Web Button design and production

I need remote control like buttons (or your own design of buttons if I like it)
3x4 text buttons (normal, pressed, disabled)
3x1 empty button (normal, pressed, disabled)
3x6 buttons with glyph (normal, pressed, disabled)
3x288 with 24h time "00:00", "00:05", "00:10" (normal, pressed, disabled)
4 LED (red, green, orange, black)
I will upload the background image as soon as possible (black plastic)
See attached images
Q: Do the buttons have to be gray/black?
A: It should look like a high end remote control. It could be brushed aluminum as well, or something you come up with. But I guess black or dark grey would be best. The background will be picsharbor 40561739, but it's not available yet.
Q: Do I have to provide all buttons for the contest?
A: No! I only need one button (3 states) and a LED to decide. Only the winner will do the whole job.
Q: Is the Designer who wins the contest expected to complete all the extra buttons?
A: Yes, please.
Plastic

```html
<!DOCTYPE html>
<html lang="en">
<head>
<meta charset="utf-8">
<title>Remote Control Button Kit</title>
<link href="https://fonts.googleapis.com/css2?family=Quicksand:wght@300;400;500&display=swap" rel="stylesheet">
<style>
  :root{
    --page:#ffffff;
    --panel-line:#d6d6d8;
    --btn-top:#54555c;
    --btn-bottom:#2f3036;
    --btn-edge:#1d1e22;
    --btn-press-top:#2a2b30;
    --btn-press-bottom:#3a3b41;
    --glyph:#b9bac0;
    --label:#6e6e72;
    --label-faint:#e2e2e4;
    --disabled-face:#ffffff;
    --disabled-edge:#d8d8da;
    --ring:#cfcfd1;
    --led-green:#36c23a;
    --led-red:#e01b1b;
    --led-orange:#e6a01a;
    --led-black:#1a1a1a;
    --key-a:#a6a020;
    --key-b:#b5161a;
    --key-c:#1f4fb5;
  }
  html,body{margin:0;padding:0;}
  body{
    width:837px;height:1200px;overflow:hidden;position:relative;
    background:var(--page);
    font-family:"Quicksand",sans-serif;
  }
  .abs{position:absolute;}

  /* LEDs */
  .led{position:absolute;top:50px;width:34px;height:34px;border-radius:50%;
    background:#2b2b2b;box-shadow:0 1px 2px rgba(0,0,0,.35);}
  .led::after{content:"";position:absolute;left:7px;top:7px;width:20px;height:20px;border-radius:50%;
    background:radial-gradient(circle at 45% 40%,rgba(255,255,255,.55),var(--c) 45%,var(--c) 100%);}
  .led--green{left:301px;--c:var(--led-green);}
  .led--red{left:373px;--c:var(--led-red);}
  .led--orange{left:438px;--c:var(--led-orange);}
  .led--black{left:505px;--c:var(--led-black);}
  .led--black::after{width:14px;height:14px;left:10px;top:10px;background:#050505;}

  /* State panel */
  .state-panel{position:absolute;left:77px;top:130px;width:682px;height:342px;
    border:1.5px solid var(--panel-line);border-radius:14px;}
  .state-label{position:absolute;top:142px;width:200px;margin-left:-100px;text-align:center;
    font-size:21px;font-weight:300;color:var(--label);}

  .btn{position:absolute;box-sizing:border-box;display:flex;align-items:center;justify-content:center;
    border-radius:8px;border:1.5px solid var(--btn-edge);
    background:linear-gradient(var(--btn-top),var(--btn-bottom));
    box-shadow:inset 0 1px 0 rgba(255,255,255,.18),0 2px 3px rgba(0,0,0,.35);
    color:var(--glyph);font-weight:300;}
  .btn--pressed{background:linear-gradient(var(--btn-press-top),var(--btn-press-bottom));
    box-shadow:inset 0 3px 6px rgba(0,0,0,.7),0 1px 1px rgba(255,255,255,.4);color:#8c8d93;}
  .btn--disabled{background:var(--disabled-face);border-color:var(--disabled-edge);
    box-shadow:inset 0 -2px 4px rgba(0,0,0,.08),0 1px 2px rgba(0,0,0,.12);
    color:#fff;-webkit-text-stroke:1px #444;}
  .btn--text{top:186px;width:189px;height:58px;font-size:29px;}
  .btn--time{top:301px;width:92px;height:65px;font-size:28px;border-radius:10px;}
  .btn--link{top:404px;width:137px;height:44px;font-size:18px;font-weight:500;border-radius:3px;}

  .text-link{position:absolute;left:113px;top:414px;font-size:18px;font-weight:500;color:var(--label);
    text-decoration:underline;}
  .link-rule{position:absolute;left:233px;top:437px;width:85px;border-top:1.5px solid var(--panel-line);}

  /* Media transport */
  .media-label{position:absolute;top:518px;width:110px;margin-left:-55px;text-align:center;
    font-size:18px;line-height:17px;color:var(--label-faint);}
  .btn--media{top:547px;width:94px;height:63px;border-radius:10px;}
  .btn--media svg{width:34px;height:34px;fill:var(--glyph);}

  /* Navigation */
  .nav-pad{position:absolute;left:219px;top:658px;width:376px;height:376px;}
  .rocker{position:absolute;top:744px;width:75px;height:198px;box-sizing:border-box;border-radius:38px;
    border:1.5px solid var(--btn-edge);background:linear-gradient(var(--btn-top),var(--btn-bottom));
    box-shadow:inset 0 1px 0 rgba(255,255,255,.18),0 2px 4px rgba(0,0,0,.35);
    color:var(--glyph);font-size:21px;font-weight:300;text-align:center;}
  .rocker--vol{left:115px;}
  .rocker--ch{left:636px;}
  .rocker span{position:absolute;left:0;right:0;top:86px;}
  .rocker svg{position:absolute;left:25px;width:24px;height:20px;fill:var(--glyph);}

  /* Colour keys */
  .key{position:absolute;}
</style>
</head>
<body>
  <div class="led led--green"></div>
  <div class="led led--red"></div>
  <div class="led led--orange"></div>
  <div class="led led--black"></div>

  <div class="state-panel"></div>
  <div class="state-label" style="left:188px">On</div>
  <div class="state-label" style="left:419px">Depressed</div>
  <div class="state-label" style="left:643px">Disabled</div>

  <div class="btn btn--text" style="left:97px">Text</div>
  <div class="btn btn--text btn--pressed" style="left:325px">Text</div>
  <div class="btn btn--text btn--disabled" style="left:551px;top:188px;height:54px">Text</div>

  <div class="btn btn--time" style="left:142px">17:25</div>
  <div class="btn btn--time btn--pressed" style="left:370px">17:25</div>
  <div class="btn btn--time btn--disabled" style="left:597px">17:25</div>

  <a class="text-link">Text Link</a>
  <div class="link-rule"></div>
  <div class="btn btn--link" style="left:438px;color:#9a9ba1">Text Link</div>
  <div class="btn btn--link btn--pressed" style="left:592px;color:#e6e6e8">Text Link</div>

  <div class="media-label" style="left:124px">Play</div>
  <div class="media-label" style="left:244px;top:500px">Fast Forward</div>
  <div class="media-label" style="left:363px">Rewind</div>
  <div class="media-label" style="left:483px">Stop</div>
  <div class="media-label" style="left:603px">Pause</div>
  <div class="media-label" style="left:722px">Go Back</div>

  <div class="btn btn--media" style="left:77px"><svg viewBox="0 0 34 34"><path d="M11 8 L26 17 L11 26 Z"/></svg></div>
  <div class="btn btn--media" style="left:197px"><svg viewBox="0 0 34 34"><path d="M4 9 L17 17 L4 25 Z M17 9 L30 17 L17 25 Z"/></svg></div>
  <div class="btn btn--media" style="left:316px"><svg viewBox="0 0 34 34"><path d="M30 9 L17 17 L30 25 Z M17 9 L4 17 L17 25 Z"/></svg></div>
  <div class="btn btn--media" style="left:436px"><svg viewBox="0 0 34 34"><rect x="8" y="8" width="18" height="18"/></svg></div>
  <div class="btn btn--media" style="left:556px"><svg viewBox="0 0 34 34"><rect x="9" y="8" width="6" height="18"/><rect x="19" y="8" width="6" height="18"/></svg></div>
  <div class="btn btn--media" style="left:675px"><svg viewBox="0 0 34 34"><path d="M6 13 L13 6 L13 10 L18 10 A8.5 8.5 0 0 1 18 27 L12 27 L12 22 L18 22 A3.5 3.5 0 0 0 18 15 L13 15 L13 20 Z"/></svg></div>

  <svg class="nav-pad" viewBox="-188 -188 376 376">
    <defs>
      <linearGradient id="pad-fill" x1="0" y1="0" x2="0" y2="1">
        <stop offset="0" stop-color="#55565d"/><stop offset="1" stop-color="#2f3036"/>
      </linearGradient>
      <g id="pad-sector">
        <path d="M-94.9 -121.4 A154 154 0 0 1 94.9 -121.4 L38.8 -49.6 A63 63 0 0 0 -38.8 -49.6 Z" fill="url(#pad-fill)" stroke="#1d1e22" stroke-width="1.5"/>
        <path d="M-9 -110 L0 -124 L9 -110 Z" fill="#b9bac0"/>
      </g>
    </defs>
    <circle r="185" fill="#fff" stroke="var(--ring)" stroke-width="3"/>
    <use href="#pad-sector"/>
    <use href="#pad-sector" transform="rotate(90)"/>
    <use href="#pad-sector" transform="rotate(180)"/>
    <use href="#pad-sector" transform="rotate(270)"/>
    <circle r="48" fill="url(#pad-fill)" stroke="#1d1e22" stroke-width="1.5"/>
    <text y="10" text-anchor="middle" font-family="Quicksand, sans-serif" font-weight="300" font-size="28" fill="#b9bac0">GO</text>
  </svg>

  <div class="rocker rocker--vol">
    <svg viewBox="0 0 24 20" style="top:22px"><path d="M2 18 L12 2 L22 18 Z"/></svg>
    <span>VOL</span>
    <svg viewBox="0 0 24 20" style="bottom:22px"><path d="M2 2 L22 2 L12 18 Z"/></svg>
  </div>
  <div class="rocker rocker--ch">
    <svg viewBox="0 0 24 20" style="top:22px"><path d="M2 18 L12 2 L22 18 Z"/></svg>
    <span>CH</span>
    <svg viewBox="0 0 24 20" style="bottom:22px"><path d="M2 2 L22 2 L12 18 Z"/></svg>
  </div>

  <svg class="key" style="left:272px;top:1062px" width="62" height="58" viewBox="0 0 62 58">
    <path d="M31 3 L59 55 L3 55 Z" fill="var(--key-a)" stroke="#5e5a10" stroke-width="1.5"/>
    <text x="31" y="48" text-anchor="middle" font-family="Quicksand, sans-serif" font-size="18" fill="#1e1e10">A</text>
  </svg>
  <svg class="key" style="left:383px;top:1062px" width="58" height="58" viewBox="0 0 58 58">
    <circle cx="29" cy="29" r="26" fill="var(--key-b)" stroke="#5a0a0b" stroke-width="1.5"/>
    <text x="29" y="36" text-anchor="middle" font-family="Quicksand, sans-serif" font-size="19" fill="#f4dede">B</text>
  </svg>
  <svg class="key" style="left:497px;top:1065px" width="52" height="52" viewBox="0 0 52 52">
    <rect x="2" y="2" width="48" height="48" fill="var(--key-c)" stroke="#0e2456" stroke-width="1.5"/>
    <text x="26" y="33" text-anchor="middle" font-family="Quicksand, sans-serif" font-size="19" fill="#e2e8f6">C</text>
  </svg>
</body>
</html>
```